Business Cards + Flyer + Letterhead for Care Recruitment Agency

We are a recruitment agency for the health & care sector. We need designs made for business cards, A5 double-sided flyer, and a letterhead template.

Our branding message is professionalism, care, compassion, expertise. We are experts in recruitment for the care & health industry.

Our logo source files and colours are here - https://www.filevault-example.net/sh/qplr82nvzkx/BBKdLm4ORTe93pWqHnZxYa?dl=0

For the business card, I have attached an example we like. We want a vertical business card design, something very similar to the example given. The design should match our logo in terms of brand colors. On one side should be our logo, our website (www.penhollowbrook.co.uk) and Care Recruitment Specialists written somewhere visible that fits, between our logo and the website at the bottom. On the other side should be our details.

Details on the front:

Logo with slogan
Care Recruitment Specialists
www.penhollowbrook.co.uk

Details on the back:

Marcus Ellory
Managing Director

Rowan Court, 41-47 Tillwick St, Birmingham, B9 7QX
07612 459073
marcus@penhollowbrook.co.uk
www.penhollowbrook.co.uk

Deirdre Penhollow
Business Development Director

07831 204968
deirdre@penhollowbrook.co.uk
www.penhollowbrook.co.uk

For the A5 flyer, I have attached some pictures we've used for the website, which could be used for the flyer as well. To get a better idea of our branding, please visit our website - https://penhollowbrook.co.uk/

The text for the flyer is also attached.

Finally, the letterhead template should be a docx template with our logo and our identifiable branding (the same shapes and matching colours you will come up with for the business cards and flyer).

```html
<!DOCTYPE html>
<html lang="en">
<head>
<meta charset="utf-8">
<title>Penhollow Brook – Business Card</title>
<link rel="stylesheet" href="https://fonts.googleapis.com/css2?family=Montserrat:wght@500;700;800&family=Roboto:wght@400;500;700&display=swap">
<style>
  :root {
    --backdrop: #d6d6d4;
    --card-white: #ffffff;
    --navy: #13275f;
    --brand-blue: #0f7fe8;
    --sky: #17a6f2;
    --text-grey: #4a4a4a;
    --blue-deep: #0a30a6;
    --blue-night: #161b37;
    --emboss: #2a4cb8;
    --specialists: #c9d2ea;
  }
  * { box-sizing: border-box; margin: 0; padding: 0; }
  html, body { width: 1200px; height: 801px; overflow: hidden; }
  body {
    background: var(--backdrop);
    position: relative;
    font-family: "Roboto", Arial, sans-serif;
  }

  /* Details side (vertical) */
  .card-details {
    position: absolute;
    left: 170px; top: 137px;
    width: 340px; height: 527px;
    background: var(--card-white);
    box-shadow: 0 2px 6px rgba(0,0,0,.15);
    padding: 0 36px;
  }
  .brand-lockup {
    position: absolute;
    top: 120px; left: 0; right: 0;
    display: flex; flex-direction: column; align-items: center; gap: 18px;
  }
  .brand-mark {
    width: 58px; height: 58px; border-radius: 50%;
    background: var(--brand-blue);
  }
  .brand-name {
    font-family: "Montserrat", Arial, sans-serif;
    font-weight: 800;
    font-size: 25px;
    letter-spacing: 2px;
    color: var(--navy);
    text-transform: uppercase;
  }
  .contact {
    position: absolute;
    left: 36px; bottom: 44px;
    color: var(--text-grey);
  }
  .person-name {
    font-family: "Montserrat", Arial, sans-serif;
    font-weight: 800;
    font-size: 19px;
    letter-spacing: .5px;
    color: var(--sky);
    text-transform: uppercase;
  }
  .person-role {
    font-weight: 700;
    font-size: 14.5px;
    margin: 2px 0 14px;
  }
  .address { font-size: 14.5px; line-height: 1.3; margin-bottom: 6px; }
  .contact-line {
    display: flex; align-items: center; gap: 7px;
    font-size: 14.5px; line-height: 1.45;
  }
  .contact-line svg { width: 13px; height: 13px; flex: none; }

  /* Brand side (horizontal) */
  .card-brand {
    position: absolute;
    left: 572px; top: 237px;
    width: 527px; height: 340px;
    background: linear-gradient(115deg, var(--blue-deep) 0%, #0d2a86 45%, var(--blue-night) 100%);
    box-shadow: 0 2px 6px rgba(0,0,0,.2);
    color: var(--specialists);
  }
  .brand-lockup-dark {
    position: absolute;
    top: 112px; left: 0; right: 0;
    display: flex; align-items: center; justify-content: center; gap: 18px;
  }
  .brand-mark-dark {
    width: 52px; height: 52px; border-radius: 50%;
    background: var(--emboss);
  }
  .brand-name-dark {
    font-family: "Montserrat", Arial, sans-serif;
    font-weight: 800;
    font-size: 30px;
    letter-spacing: 3px;
    color: var(--emboss);
    text-transform: uppercase;
  }
  .specialists {
    position: absolute;
    left: 0; right: 0; bottom: 70px;
    text-align: center;
    font-family: "Montserrat", Arial, sans-serif;
    font-weight: 500;
    font-size: 14px;
    letter-spacing: 1px;
  }
</style>
</head>
<body>

<section class="card-details">
  <div class="brand-lockup">
    <div class="brand-mark"></div>
    <div class="brand-name">Penhollow Brook</div>
  </div>

  <div class="contact">
    <p class="person-name">Marcus Ellory</p>
    <p class="person-role">Managing Director</p>
    <p class="address">Rowan Court,<br>41-47 Tillwick St,<br>Birmingham, B9 7QX</p>
    <p class="contact-line">
      <svg viewBox="0 0 16 16" aria-hidden="true"><path fill="#1a8fe8" d="M3 1h3l1.5 4-2 1.3a9 9 0 0 0 4.2 4.2L11 8.5l4 1.5v3a2 2 0 0 1-2 2A12 12 0 0 1 1 3a2 2 0 0 1 2-2z"/></svg>
      07612 459073
    </p>
    <p class="contact-line">
      <svg viewBox="0 0 16 16" aria-hidden="true"><rect x="1" y="3" width="14" height="10" fill="#1a8fe8"/><path d="M1 3l7 6 7-6" fill="none" stroke="#fff" stroke-width="1.3"/></svg>
      marcus@penhollowbrook.co.uk
    </p>
    <p class="contact-line">
      <svg viewBox="0 0 16 16" aria-hidden="true"><circle cx="8" cy="8" r="7" fill="#1a8fe8"/><path d="M1 8h14M8 1c-3 3-3 11 0 14M8 1c3 3 3 11 0 14" fill="none" stroke="#fff" stroke-width="1"/></svg>
      www.penhollowbrook.co.uk
    </p>
  </div>
</section>

<section class="card-brand">
  <div class="brand-lockup-dark">
    <div class="brand-mark-dark"></div>
    <div class="brand-name-dark">Penhollow Brook</div>
  </div>
  <p class="specialists">CARE RECRUITMENT SPECIALISTS</p>
</section>

</body>
</html>
```